Art for parenting podcast with straight/direct talk...no fluff here! "Plain Answers for Families"

I need an image that will not look fluffy or soft. A no-nonsense look. This is not a 'I love parenting' podcast. It is for frustrated parents who don't know what to do. The name is 'Plain Answers for Families'. The design should, therefore, NOT have hearts and flowers but, instead, look clean and direct. My logo has shades of blue so that would be nice. I have done this work for over 30 years and am well-degreed so would like the design to look stable/established. I have attached my company's logo.

Target Market(s)

Frustrated parents of children - age birth to 20

Industry/Entity Type

Coaching/Counseling for parents

Font styles to use
Serif
Sans Serif

Colors
0054AA
0677BA
7BADD7
CADEEF
E8F1F8

Requirements
Must have
• A look that is clean/bold/direct and professional. Serious.
Nice to have
• If it looks good, my name with my degrees behind my name. MS, MEd. Another thought would be to have a background image of a frustrated parent. Not sure if that would be good or look too busy.
Should not have
• Flowers, fluff, soft appearance, pinks, light colors

```html
<!DOCTYPE html>
<html lang="en">
<head>
<meta charset="UTF-8">
<title>Plain Answers for Families — Podcast Cover</title>
<link href="https://fonts.googleapis.com/css2?family=Bebas+Neue&family=Fira+Sans+Condensed:wght@600&display=swap" rel="stylesheet">
<style>
  :root {
    --red-bright: #e01a30;
    --red-deep: #a80c1c;
    --mouth-dark: #0a0204;
    --mouth-mid: #3a050c;
    --text-white: #ffffff;
    --brand-blue: #0677ba;
    --shadow: rgba(60, 0, 8, 0.45);
  }
  html, body {
    margin: 0;
    padding: 0;
    width: 1200px;
    height: 1200px;
    overflow: hidden;
    background: var(--red-deep);
  }
  .cover {
    position: relative;
    width: 1200px;
    height: 1200px;
    overflow: hidden;
    background: linear-gradient(120deg, var(--red-bright) 0%, #d01428 55%, var(--red-deep) 100%);
  }
  .cover__photo {
    position: absolute;
    inset: 0;
    background:
      radial-gradient(ellipse 405px 495px at 372px 567px,
        var(--mouth-dark) 0%,
        #120306 55%,
        var(--mouth-mid) 80%,
        #f0f0f0 85%,
        #e8e8e8 88%,
        #c01224 93%,
        transparent 100%);
  }
  .brand {
    position: absolute;
    left: 90px;
    top: 256px;
    width: 220px;
    display: flex;
    flex-direction: column;
    align-items: center;
    gap: 12px;
  }
  .brand__dot {
    width: 44px;
    height: 44px;
    border-radius: 50%;
    background: var(--brand-blue);
  }
  .brand__name {
    font-family: "Fira Sans Condensed", sans-serif;
    font-weight: 600;
    font-size: 30px;
    line-height: 1.05;
    color: var(--brand-blue);
    text-transform: uppercase;
    letter-spacing: 1px;
    text-align: center;
  }
  .title {
    position: absolute;
    left: 356px;
    top: 218px;
    margin: 0;
    font-family: "Bebas Neue", sans-serif;
    font-weight: 400;
    color: var(--text-white);
    text-shadow: 3px 4px 6px var(--shadow);
    line-height: 1;
  }
  .title__line {
    display: block;
    font-size: 236px;
    line-height: 242px;
    letter-spacing: 1px;
    white-space: nowrap;
  }
  .title__small {
    font-size: 116px;
    letter-spacing: 1px;
    margin-left: 14px;
  }
  .host {
    position: absolute;
    left: 555px;
    top: 1066px;
    margin: 0;
    font-family: "Fira Sans Condensed", sans-serif;
    font-weight: 600;
    font-size: 46px;
    color: var(--text-white);
    text-shadow: 2px 3px 4px var(--shadow);
    white-space: nowrap;
  }
  .host__degrees {
    margin-left: 34px;
  }
</style>
</head>
<body>
  <main class="cover">
    <div class="cover__photo" role="img" aria-label="Close-up photograph of a wide open mouth with red lips and white teeth, shouting"></div>

    <div class="brand">
      <span class="brand__dot"></span>
      <span class="brand__name">Brightpath<br>Parenting</span>
    </div>

    <h1 class="title">
      <span class="title__line">Plain</span>
      <span class="title__line">Answers<span class="title__small">for</span></span>
      <span class="title__line">Families</span>
    </h1>

    <p class="host">Dana Whitfield<span class="host__degrees">MS, MEd</span></p>
  </main>
</body>
</html>
```